RUV Coffee bag (front and back)

We use black matte bags and have front and back labels. We have a logo but need an attractive and inviting label. The labels will be used for our entire line of coffees. We sell most of our coffee to foodservice establishments (Restaurants, Hotels, Bakeries, Bodegas) and we would like to have these establishments display our bags of coffee to sell retail.
The logo can be used as a whole or using any one of the three components (Logo, image, tag).

Target Market(s)

People who buy the coffee they brew at home from the local shop they get their morning latte.. We are a local coffee company, but we do not sell locally roasted coffee!

Industry/Entity Type

Food

Font styles to use
Other font styles liked:
• something that looks good with our trademarked RUV

Colors

Designer to choose colors to be used in the design.

Requirements
Must have
• Respect Trademarked logo
Nice to have
• It would be nice to have a design that can be used with other mediums (airpot wraps, java jackets, )
Should not have
• Real People

```html
<!DOCTYPE html>
<html lang="en">
<head>
<meta charset="utf-8">
<title>RUV Coffee – Bag Labels</title>
<link href="https://fonts.googleapis.com/css2?family=Poppins:wght@200;300;600;700&family=Playfair+Display:wght@900&family=Great+Vibes&family=Source+Sans+3:wght@400;700&family=Roboto+Slab:wght@700&display=swap" rel="stylesheet">
<style>
  :root {
    --bg: #f0f0f0;
    --ink: #111111;
    --bag: #121212;
    --bag-soft: #1c1c1c;
    --red: #e5262d;
    --red-deep: #c81f26;
    --white: #f4f4f4;
    --rule: #bdbdbd;
  }
  * { margin: 0; padding: 0; box-sizing: border-box; }
  html, body { width: 1009px; height: 1200px; overflow: hidden; }
  body {
    position: relative;
    background: var(--bg);
    font-family: "Poppins", sans-serif;
    color: var(--white);
  }

  /* Brand header */
  .brand-header { position: absolute; left: 0; top: 0; width: 100%; height: 330px; color: var(--ink); text-align: center; }
  .brand-dot {
    position: absolute; left: 50%; top: 94px; width: 24px; height: 24px; margin-left: -12px;
    border-radius: 50%; background: var(--red);
  }
  .brand-name {
    position: absolute; left: 0; top: 184px; width: 100%;
    font-weight: 200; font-size: 130px; line-height: 1; letter-spacing: 6px;
  }
  .brand-tag {
    position: absolute; left: 0; top: 299px; width: 100%;
    font-size: 11px; letter-spacing: 6px; font-weight: 300;
  }

  /* Label panels */
  .label {
    position: absolute; top: 359px; width: 354px; height: 771px;
    background: linear-gradient(180deg, var(--bag-soft) 0%, var(--bag) 45%, var(--bag-soft) 100%);
    overflow: hidden; text-align: center;
  }
  .label--front { left: 121px; }
  .label--back { left: 535px; }
  .label .texture { position: absolute; inset: 0 0 54px 0; background: radial-gradient(ellipse at 50% 40%, rgba(255,255,255,0.04), rgba(0,0,0,0) 70%); }
  .label .band {
    position: absolute; left: 0; bottom: 0; width: 100%; height: 54px;
    background: linear-gradient(180deg, var(--red) 0%, var(--red-deep) 100%);
    font-size: 10.5px; padding-top: 9px; color: var(--white);
  }
  .abs { position: absolute; left: 0; width: 100%; }

  .label .mark-ring {
    position: absolute; left: 50%; top: 243px; width: 92px; height: 92px; margin-left: -46px;
    border: 6px solid var(--red); border-radius: 50%;
  }
  .label .name { top: 346px; font-weight: 200; font-size: 86px; line-height: 1; letter-spacing: 4px; color: var(--white); }
  .label .tag { top: 424px; font-size: 8px; letter-spacing: 3px; font-weight: 300; }

  /* Front */
  .product-frame {
    position: absolute; left: 35px; top: 441px; width: 285px; height: 156px;
    border: 1px solid var(--rule); background: #000;
  }
  .product-name { font-family: "Playfair Display", serif; font-weight: 900; color: var(--white); line-height: 1; }
  .product-name.top { top: 452px; font-size: 50px; }
  .product-name.crema { top: 500px; font-size: 52px; letter-spacing: 1px; }
  .product-script {
    top: 520px; left: 6px; font-family: "Great Vibes", cursive; font-size: 96px; line-height: 1; color: var(--red);
  }
  .blend { top: 608px; font-size: 14px; font-weight: 300; line-height: 16.5px; }
  .roast { top: 680px; font-size: 20px; font-weight: 700; color: var(--red); letter-spacing: 0.5px; }

  .divider { display: flex; align-items: center; justify-content: center; gap: 8px; }
  .divider::before, .divider::after { content: ""; width: 76px; height: 1px; background: var(--rule); }
  .divider .bean { width: 9px; height: 13px; border-radius: 50%; background: var(--white); transform: rotate(25deg); }
  .front-divider { top: 665px; }

  /* Back */
  .section-title { color: var(--red); font-weight: 700; }
  .back .brewing-title { top: 444px; font-family: "Roboto Slab", serif; font-size: 22px; }
  .back .copy { font-family: "Source Sans 3", sans-serif; font-size: 14.5px; line-height: 18px; color: var(--white); }
  .back .brewing-copy { top: 473px; }
  .back .div-1 { top: 537px; }
  .back .storing-title { top: 555px; font-family: "Poppins", sans-serif; font-size: 21px; }
  .back .storing-copy { top: 584px; }
  .back .div-2 { top: 632px; }
  .back .dist-title { top: 653px; font-family: "Poppins", sans-serif; font-size: 12px; }
  .back .dist-copy { top: 669px; line-height: 16px; }
</style>
</head>
<body>

  <header class="brand-header">
    <span class="brand-dot"></span>
    <div class="brand-name">RUV</div>
    <div class="brand-tag">Ridge Union Valley Coffee</div>
  </header>

  <section class="label label--front" aria-label="Front label">
    <div class="texture" role="img" aria-label="Subtle tonal pattern of coffee leaves and beans on black"></div>
    <div class="mark-ring"></div>
    <div class="abs name">RUV</div>
    <div class="abs tag">Ridge Union Valley Coffee</div>

    <div class="product-frame"></div>
    <div class="abs product-name top">RUBY</div>
    <div class="abs product-name crema">CREMA</div>
    <div class="abs product-script">espresso</div>

    <div class="abs blend">A Rich<br>Classic<br>Espresso Blend</div>
    <div class="abs divider front-divider"><span class="bean"></span></div>
    <div class="abs roast">ESPRESSO ROAST</div>

    <div class="band">2 lb. Whole Bean Coffee</div>
  </section>

  <section class="label label--back back" aria-label="Back label">
    <div class="texture" role="img" aria-label="Subtle tonal pattern of coffee leaves and beans on black"></div>
    <div class="mark-ring"></div>
    <div class="abs name">RUV</div>
    <div class="abs tag">Ridge Union Valley Coffee</div>

    <h2 class="abs section-title brewing-title">BREWING</h2>
    <p class="abs copy brewing-copy">Use fresh filtered cold water.<br>Measure 2 TBSP of coffee for every 6 oz. of water.<br>Brew with water 195°F - 205°F</p>
    <div class="abs divider div-1"><span class="bean"></span></div>

    <h2 class="abs section-title storing-title">STORING</h2>
    <p class="abs copy storing-copy">Store in an airtight container in a cool, dry place.<br>Do not freeze.</p>
    <div class="abs divider div-2"><span class="bean"></span></div>

    <h3 class="abs section-title dist-title">DISTRIBUTED BY</h3>
    <p class="abs copy dist-copy">Ridge Union Valley Coffee Company LLC<br>123-456-7890 &nbsp;|&nbsp; info@ruvcoffee.com</p>

    <div class="band">2 lb. Whole Bean Coffee</div>
  </section>

</body>
</html>
```